Verdant Pathworks Business Card

want the back of card to be blue- with the logo in the center
front of card- info plus logo (info being mailing address, email address, and website address )
4 different names with titles to have on cards
1) Dominic Ashvale - Owner
2) Bethany Korvuth- Customer Relationship Specialist
3) Luca Brennwick- Vice President of Sales
4) Neil Umbright- Chief Technology Officer

Target Market(s)

tech company in the government/probation office industry

Industry/Entity Type

Government Office

Contact Information for Business Card

1) Dominic Ashvale - Owner

Colors
0355a3
ffffff

Requirements
Must have
• back side should be blue, with the logo placed in the center
• front side needs to include both the logo, as well as company info (info should include website address, email address, and mailing address)

```html
<!DOCTYPE html>
<html lang="en">
<head>
<meta charset="utf-8">
<title>Verdant Pathworks Business Card</title>
<link href="https://fonts.googleapis.com/css2?family=Roboto:wght@400;500;700&display=swap" rel="stylesheet">
<style>
  :root {
    --navy: #152c54;
    --white: #ffffff;
    --grey-text: #7d7d80;
    --ink: #1c2a44;
    --stage: #e6e7e8;
    --shadow: rgba(0, 0, 0, 0.22);
  }
  * { margin: 0; padding: 0; box-sizing: border-box; }
  html, body {
    width: 1200px;
    height: 1006px;
    overflow: hidden;
    background: var(--stage);
    font-family: "Roboto", Arial, sans-serif;
  }
  .canvas { position: relative; width: 1200px; height: 1006px; }
  .card {
    position: absolute;
    left: 254px;
    width: 692px;
    height: 393px;
    box-shadow: 0 8px 22px var(--shadow);
  }
  .card-back {
    top: 105px;
    background: var(--navy);
    display: flex;
    flex-direction: column;
    align-items: center;
    justify-content: center;
    gap: 26px;
  }
  .card-front { top: 540px; background: var(--white); }

  .brand-mark { display: block; }
  .brand-name {
    font-weight: 500;
    text-transform: uppercase;
    text-align: center;
    line-height: 1.1;
  }
  .card-back .brand-name {
    color: var(--white);
    font-size: 50px;
    letter-spacing: 4px;
  }

  .front-brand {
    position: absolute;
    left: 0;
    top: 0;
    width: 346px;
    height: 100%;
    display: flex;
    flex-direction: column;
    align-items: center;
    justify-content: center;
    gap: 18px;
  }
  .front-brand .brand-name {
    color: var(--navy);
    font-size: 30px;
    letter-spacing: 2px;
  }

  .divider {
    position: absolute;
    left: 345px;
    top: 74px;
    width: 3px;
    height: 245px;
    background: var(--navy);
  }

  .contact-block { position: absolute; left: 385px; top: 107px; }
  .person-name {
    color: var(--navy);
    font-size: 30px;
    font-weight: 700;
    line-height: 1.1;
  }
  .person-title {
    color: var(--grey-text);
    font-size: 21px;
    margin-top: 4px;
  }
  .contact-list { list-style: none; margin-top: 30px; }
  .contact-list li {
    display: flex;
    align-items: center;
    gap: 12px;
    color: var(--ink);
    font-size: 18px;
    height: 25.5px;
  }
  .contact-list svg { width: 14px; height: 14px; flex: none; }
</style>
</head>
<body>
<main class="canvas">

  <section class="card card-back" aria-label="Card back">
    <svg class="brand-mark" width="84" height="84" viewBox="0 0 84 84" aria-hidden="true">
      <rect x="3" y="3" width="78" height="78" fill="none" stroke="var(--white)" stroke-width="5"/>
    </svg>
    <h1 class="brand-name">Verdant Pathworks</h1>
  </section>

  <section class="card card-front" aria-label="Card front">
    <div class="front-brand">
      <svg class="brand-mark" width="52" height="52" viewBox="0 0 52 52" aria-hidden="true">
        <rect x="2.5" y="2.5" width="47" height="47" fill="none" stroke="var(--navy)" stroke-width="4"/>
      </svg>
      <p class="brand-name">Verdant Pathworks</p>
    </div>

    <div class="divider"></div>

    <div class="contact-block">
      <p class="person-name">Dominic Ashvale</p>
      <p class="person-title">Owner</p>
      <ul class="contact-list">
        <li>
          <svg viewBox="0 0 14 14" aria-hidden="true"><path d="M7 1.2a4 4 0 0 0-4 4c0 3 4 7.6 4 7.6s4-4.6 4-7.6a4 4 0 0 0-4-4z" fill="none" stroke="var(--ink)" stroke-width="1.3"/><circle cx="7" cy="5.2" r="1.4" fill="var(--ink)"/></svg>
          48 Larkmere Road, Suite 100
        </li>
        <li>
          <svg viewBox="0 0 14 14" aria-hidden="true"><path d="M3 1.5l2.2 2.6-1.2 1.6a8 8 0 0 0 4.3 4.3l1.6-1.2 2.6 2.2-1.3 1.5C6.5 12.4 1.6 7.5 1.5 2.8z" fill="none" stroke="var(--ink)" stroke-width="1.2" stroke-linejoin="round"/></svg>
          +123 555 0142
        </li>
        <li>
          <svg viewBox="0 0 14 14" aria-hidden="true"><rect x="1.5" y="3" width="11" height="8" fill="none" stroke="var(--ink)" stroke-width="1.2"/><path d="M1.5 3.5L7 7.8l5.5-4.3" fill="none" stroke="var(--ink)" stroke-width="1.2"/></svg>
          dominic@verdantpath.com
        </li>
        <li>
          <svg viewBox="0 0 14 14" aria-hidden="true"><circle cx="7" cy="7" r="5.5" fill="none" stroke="var(--ink)" stroke-width="1.2"/><ellipse cx="7" cy="7" rx="2.3" ry="5.5" fill="none" stroke="var(--ink)" stroke-width="1"/><path d="M1.5 7h11" stroke="var(--ink)" stroke-width="1"/></svg>
          www.verdantpath.com
        </li>
      </ul>
    </div>
  </section>

</main>
</body>
</html>
```